Spice Mix Label Bottle Branding - Health and Weight Loss Mixes

The company is called ZestRow Spice Mix's. We've created 5 spice mixes using ingredients that promote health and weight loss. We already have a logo but now we need labels for our bottles. We would like to see designs that have the feel of health supplements (see attached examples)

We would like a different colour featured with each of our flavours.

Our flavours are:
-Golden Chai (Yellow)
-Mild Curry (Orange)
-Coffee Rub (brown)
-Garlic Oregano (Green)
-Taco (Blue)

Thank you!

Target Market(s)

Ages 22-35. Men and Female. Trendy, Hipster.

Industry/Entity Type

Food Production

Font styles to use
Sans Serif

Colors
f37122
0655a3
0692cd
9bcb3c
fbee3f

Requirements
Must have
• A different featured colour for each flavour.
• The ZestRow Spices Logo (attached)
• The slogan: "Weight Loss Ingredients"
• -Golden Chai (Yellow)
• -Mild Curry (Orange)
• -Coffee Rub (brown)
• -Garlic Oregano (Green)
• -Taco (Blue)
• Text Files attached.
Nice to have
• A black label with a featured colour for each of the spice mice flavours.
• 'No Salt added'

```html
<!DOCTYPE html>
<html lang="en">
<head>
<meta charset="utf-8">
<title>ZestRow Spices – Mild Curry Label</title>
<link rel="stylesheet" href="https://fonts.googleapis.com/css2?family=Anton&family=Montserrat:wght@700;800&display=swap">
<style>
  :root {
    --ink: #1d1d1d;
    --paper: #ffffff;
    --curry: #f37122;
    --stage: #e8eae5;
    --soft-ink: #2a2a2a;
  }
  * { margin: 0; padding: 0; box-sizing: border-box; }
  html, body { width: 1200px; height: 1105px; overflow: hidden; }
  body { background: var(--stage); position: relative; font-family: "Montserrat", sans-serif; }

  .label {
    position: absolute;
    left: 100px; top: 170px;
    width: 1000px; height: 760px;
    background: var(--paper);
    overflow: hidden;
    box-shadow: 0 10px 30px rgba(0,0,0,.12);
  }
  .label-shapes { position: absolute; inset: 0; }

  .brand {
    position: absolute;
    left: 0; right: 0; top: 110px;
    text-align: center;
  }
  .brand-name {
    display: inline-flex; align-items: center; gap: 22px;
    font-family: "Anton", sans-serif;
    font-size: 130px; line-height: 1;
    color: var(--ink);
    letter-spacing: 2px;
    text-transform: uppercase;
  }
  .brand-dot {
    width: 34px; height: 34px; border-radius: 50%;
    background: var(--curry);
  }
  .brand-tagline {
    margin-top: 14px;
    font-weight: 800; font-size: 22px;
    letter-spacing: 2px;
    color: var(--ink);
    text-transform: uppercase;
  }
  .brand-rule {
    width: 330px; height: 3px; margin: 8px auto 0;
    background: var(--ink);
  }

  .flavour {
    position: absolute;
    left: 0; right: 0; top: 472px;
    text-align: center;
    font-family: "Anton", sans-serif;
    font-size: 124px; line-height: 1;
    color: var(--paper);
    letter-spacing: 4px;
    text-shadow: 6px 6px 0 var(--curry);
    text-transform: uppercase;
  }
  .slogan-band {
    position: absolute;
    left: 0; right: 0; top: 622px;
    height: 52px;
    background: var(--curry);
    display: flex; align-items: center; justify-content: center;
    font-weight: 800; font-size: 26px;
    letter-spacing: 9px;
    color: var(--soft-ink);
    text-transform: uppercase;
  }
  .net-weight {
    position: absolute;
    left: 0; right: 0; top: 694px;
    text-align: center;
    font-weight: 700; font-size: 24px;
    letter-spacing: 4px;
    color: var(--paper);
  }
</style>
</head>
<body>
  <section class="label" aria-label="ZestRow Spices Mild Curry bottle label">
    <svg class="label-shapes" width="1000" height="760" viewBox="0 0 1000 760" aria-hidden="true">
      <path d="M0,52 Q500,10 1000,70" fill="none" stroke="var(--ink)" stroke-width="6"/>
      <path d="M0,430 Q520,500 1000,405 L1000,760 L0,760 Z" fill="var(--ink)"/>
    </svg>

    <div class="brand">
      <div class="brand-name"><span class="brand-dot"></span>ZestRow Spices</div>
      <p class="brand-tagline">Weight Loss Seasonings</p>
      <div class="brand-rule"></div>
    </div>

    <h1 class="flavour">Mild Curry</h1>
    <div class="slogan-band">Weight Loss Ingredients</div>
    <p class="net-weight">NT. WT. 100 G.</p>
  </section>
</body>
</html>
```